Tressvane hair oil bottle & packaging (Instagrammable)

I'm a blogger/social media influencer and I'm launching my own hair oil that I created myself. The hair oil is something I've used fora a long time and it makes your hair grow like there's no tomorrow!

I'm looking for a feminine and minimalistic bottle for the hair oil and also a nice packaging for the bottle. Please have a look at my Instagram account (@minaveltroo), I'd love if the product design and color scheme would be inspired by my Instagram feed. I'm looking for a design that would look very 'Instagrammable'

Product name: Tressvane
Bottle size: 100ml

Thank you xx

Target Market(s)

Females

Requirements
Must have
• According to the law this has to be marked on the packaging and on the bottle:
• Amount: 100ml
• Marked on the packaging:
• Ingredients: Burdock root oil, Grapeseed oil, Organic castor oil (maybe somehow draw attention to the fact that it's organic when designing the bottle & packaging), peppermint oil, Lavender oil, Cedarwood oil, Rosemary oil
Nice to have
• I added some photos of Ai Wenna packaging - I absolutely love it! The colour is exactly what I have in mind (also if you check my Instagram it's kind of my 'feed colour' - I'd be happy if the packaging would look something like that. The Ai Wenna packaging is exactly what I meant by 'Instagrammable'.
• Also - if we go for something like this, we could write Glow up! on the inside (so you see that when opening the packaging) or feel free to come up with something yourself, just bear in mind it's a hair oil that promotes hair growth

```html
<!DOCTYPE html>
<html lang="en">
<head>
<meta charset="utf-8">
<title>Tressvane – Packaging Spread</title>
<link rel="stylesheet" href="https://fonts.googleapis.com/css2?family=Oswald:wght@500&family=Montserrat:wght@600&family=Mrs+Saint+Delafield&display=swap">
<style>
  :root {
    --backdrop: #f7f1f1;
    --blush: #f7d9da;
    --blush-deep: #f3d0d2;
    --rose-gold: #c8917b;
    --floral-dark: #b58a86;
    --floral-light: #e8c1bf;
    --ink: #1d1516;
    --cap: #1e1a1a;
    --amber-dark: #3a1a0c;
    --amber: #7a3e1c;
  }
  * { margin: 0; padding: 0; box-sizing: border-box; }
  html, body { width: 1200px; height: 1000px; overflow: hidden; }
  body { background: var(--backdrop); position: relative; font-family: "Oswald", sans-serif; }

  .panel { position: absolute; top: 152px; height: 646px; background: var(--blush); box-shadow: 0 12px 24px rgba(120, 80, 80, .12); }
  .panel--cover { left: 88px; width: 446px; }
  .panel--spine { left: 534px; width: 126px; background: var(--blush-deep); box-shadow: none; }
  .panel--inside { left: 660px; width: 446px; }

  .floral-art {
    position: absolute; inset: 0;
    background: radial-gradient(ellipse at 45% 45%, var(--floral-dark) 0%, var(--floral-light) 70%, var(--blush) 100%);
    opacity: .85;
  }

  .bottle { position: absolute; left: 498px; top: 210px; width: 196px; height: 594px; z-index: 1; }

  .label {
    position: absolute; background: var(--blush);
    border: 3px solid var(--rose-gold);
    display: flex; flex-direction: column; align-items: center; justify-content: center;
  }
  .label--cover { left: 90px; top: 252px; width: 266px; height: 146px; }
  .label--bottle { left: 526px; top: 543px; width: 140px; height: 127px; border-width: 2px; z-index: 2; }

  .wordmark { color: var(--rose-gold); font-weight: 500; letter-spacing: 1px; line-height: 1; }
  .label--cover .wordmark { font-size: 50px; }
  .label--bottle .wordmark { font-size: 25px; }

  .volume { font-family: "Montserrat", sans-serif; font-weight: 600; color: var(--ink); line-height: 1; }
  .label--cover .volume { font-size: 9px; margin-top: 14px; }
  .label--bottle .volume { font-size: 6px; margin-top: 12px; }

  .greeting {
    position: absolute; left: 68px; top: 226px; line-height: 1;
    font-family: "Mrs Saint Delafield", cursive; font-size: 96px;
    color: var(--rose-gold); transform: rotate(-8deg); white-space: nowrap;
  }
  .sign-off__xo, .sign-off__name {
    position: absolute; font-family: "Mrs Saint Delafield", cursive;
    color: var(--ink); line-height: 1; white-space: nowrap; transform: rotate(-12deg);
  }
  .sign-off__xo { left: 282px; top: 372px; font-size: 26px; }
  .sign-off__name { left: 312px; top: 392px; font-size: 54px; }
</style>
</head>
<body>
  <section class="panel panel--cover">
    <div class="floral-art" role="img" aria-label="Engraved floral illustration of roses and leaves in dusty rose tones"></div>
    <div class="label label--cover">
      <span class="wordmark">TRESSVANE</span>
      <span class="volume">100 ML</span>
    </div>
  </section>
  <section class="panel panel--spine"></section>
  <section class="panel panel--inside">
    <p class="greeting">Glow up!</p>
    <p class="sign-off"><span class="sign-off__xo">xoxo</span><span class="sign-off__name">Mina</span></p>
  </section>

  <svg class="bottle" viewBox="0 0 196 594" role="img" aria-label="Amber glass dropper bottle with black dropper cap">
    <defs>
      <linearGradient id="bottle-tone" x1="0" y1="0" x2="0" y2="1">
        <stop offset="0" stop-color="var(--cap)"/>
        <stop offset="0.3" stop-color="var(--cap)"/>
        <stop offset="0.34" stop-color="var(--amber-dark)"/>
        <stop offset="1" stop-color="var(--amber)"/>
      </linearGradient>
    </defs>
    <path fill="url(#bottle-tone)" d="M66 40 Q66 0 98 0 Q130 0 130 40 L132 110 L154 112 Q156 112 156 118 L156 182 L160 182 Q196 196 196 240 L196 578 Q196 594 180 594 L16 594 Q0 594 0 578 L0 240 Q0 196 36 182 L40 182 L40 118 Q40 112 46 112 L64 110 Z"/>
  </svg>

  <div class="label label--bottle">
    <span class="wordmark">TRESSVANE</span>
    <span class="volume">100 ML</span>
  </div>
</body>
</html>
```